We need a design for our security installation based business. Our name is K M Security Systems

We need a business card for a security installation based company. We want to look modern and professional. We would like our company logo used and the three main colours to be white, black and orange. We install intruder alarms, cctv and access control. Our preference would be to use the black/orange design on the front and orange/black on the back. Feel free to post variations.

Target Market(s)

Business owners, commercial property and large residential properties

Industry/Entity Type

Business

Contact Information for Business Card

Owen Pelham 07813 592 640

Liam Fenwick 07751 286 419

operations@kmsecuritysystems.co.uk

Intruder Alarms
CCTV
Access Control

Colors
f78f20
000000
ffffff

Requirements
Must have
• Must have the logo on the business card somewhere

```html
<!DOCTYPE html>
<html lang="en">
<head>
<meta charset="utf-8">
<title>K M Security Systems – Business Card</title>
<link href="https://fonts.googleapis.com/css2?family=Lato:wght@400;700;900&display=swap" rel="stylesheet">
<style>
  :root {
    --orange: #ef4e24;
    --black: #000000;
    --white: #ffffff;
    --stage: #2a2a2a;
    --card-w: 840px;
    --card-h: 480px;
  }
  * { box-sizing: border-box; margin: 0; padding: 0; }
  html, body { width: 1200px; height: 1200px; overflow: hidden; }
  body {
    background: var(--stage);
    font-family: "Lato", Arial, sans-serif;
    display: flex;
    flex-direction: column;
    align-items: center;
    justify-content: center;
    gap: 60px;
  }
  .card {
    width: var(--card-w);
    height: var(--card-h);
    position: relative;
    overflow: hidden;
    box-shadow: 0 14px 30px rgba(0,0,0,0.45);
  }

  /* Front */
  .card-front {
    background: var(--orange);
    display: flex;
    align-items: center;
    justify-content: center;
  }
  .brand {
    display: flex;
    align-items: center;
    gap: 22px;
    color: var(--black);
    font-weight: 900;
  }
  .brand-square {
    width: 78px;
    height: 78px;
    background: var(--black);
  }
  .brand-name {
    font-size: 56px;
    line-height: 1.05;
    letter-spacing: 1px;
    text-transform: uppercase;
  }

  /* Back */
  .card-back {
    background: var(--black);
    display: flex;
  }
  .back-band {
    width: 300px;
    height: 100%;
    background: var(--orange);
  }
  .back-details {
    flex: 1;
    padding: 62px 56px 0 70px;
    color: var(--white);
  }
  .contact {
    padding-bottom: 14px;
    margin-bottom: 18px;
    border-bottom: 3px dotted var(--orange);
  }
  .contact-name {
    color: var(--orange);
    font-weight: 700;
    font-size: 30px;
    text-transform: uppercase;
    line-height: 1.1;
  }
  .contact-line {
    display: flex;
    align-items: center;
    gap: 16px;
    font-size: 22px;
    letter-spacing: 1px;
    margin-top: 4px;
  }
  .contact-line svg { flex: none; }
  .email-line { font-size: 22px; letter-spacing: 0.5px; }
  .services { list-style: none; margin-top: 4px; }
  .service {
    display: flex;
    align-items: center;
    gap: 18px;
    font-size: 24px;
    line-height: 1.45;
  }
  .service-mark {
    width: 16px;
    height: 16px;
    background: var(--orange);
    flex: none;
  }
</style>
</head>
<body>

  <section class="card card-front" aria-label="Business card front">
    <div class="brand">
      <span class="brand-square" aria-hidden="true"></span>
      <span class="brand-name">K M Security<br>Systems</span>
    </div>
  </section>

  <section class="card card-back" aria-label="Business card back">
    <div class="back-band" aria-hidden="true"></div>
    <div class="back-details">
      <div class="contact">
        <p class="contact-name">Liam Fenwick</p>
        <p class="contact-line">
          <svg width="22" height="22" viewBox="0 0 24 24" aria-hidden="true"><path fill="#ef4e24" d="M6.6 10.8c1.4 2.8 3.8 5.1 6.6 6.6l2.2-2.2c.3-.3.7-.4 1-.2 1.1.4 2.3.6 3.6.6.6 0 1 .4 1 1V20c0 .6-.4 1-1 1C10.6 21 3 13.4 3 4c0-.6.4-1 1-1h3.5c.6 0 1 .4 1 1 0 1.3.2 2.5.6 3.6.1.3 0 .7-.2 1z"/></svg>
          07751 286 419
        </p>
      </div>
      <div class="contact">
        <p class="contact-name">Owen Pelham</p>
        <p class="contact-line">
          <svg width="22" height="22" viewBox="0 0 24 24" aria-hidden="true"><path fill="#ef4e24" d="M6.6 10.8c1.4 2.8 3.8 5.1 6.6 6.6l2.2-2.2c.3-.3.7-.4 1-.2 1.1.4 2.3.6 3.6.6.6 0 1 .4 1 1V20c0 .6-.4 1-1 1C10.6 21 3 13.4 3 4c0-.6.4-1 1-1h3.5c.6 0 1 .4 1 1 0 1.3.2 2.5.6 3.6.1.3 0 .7-.2 1z"/></svg>
          07813 592 640
        </p>
      </div>
      <div class="contact">
        <p class="contact-line email-line">
          <svg width="24" height="20" viewBox="0 0 24 20" aria-hidden="true"><rect x="1.5" y="2.5" width="21" height="15" fill="none" stroke="#ef4e24" stroke-width="2"/><path d="M1.5 2.5 L12 11 L22.5 2.5" fill="none" stroke="#ef4e24" stroke-width="2"/></svg>
          operations@kmsecuritysystems.co.uk
        </p>
      </div>
      <ul class="services">
        <li class="service"><span class="service-mark"></span>Intruder Alarms</li>
        <li class="service"><span class="service-mark"></span>CCTV</li>
        <li class="service"><span class="service-mark"></span>Access Control</li>
      </ul>
    </div>
  </section>

</body>
</html>
```